Upscale sophisticated brochure for frameless shower doors, glass and related products for a glass c

We are a small family owned glass company working in the upscale area of lower Fairfield County Connectict .We are in need of a trifold brochure with a upscale / sophisticated theme. The name of our comany is Brightpane Co. Inc.
Address- 185 West Harlow Rd. , Cos Cob, Ct. 06812 phone- 203-514-7381
It should picture and have a short discription of framless shower doors. Glass table tops for bases and furniture top protection.
Mirrored walls for exersize, yoga and workout areas, bathrooms, dressing areas
Painted glass for backsplashes.pattered glass cabinet doors.
Producs and services are listed in order of importance.
The only mention of pricing is "we are competitive in our pricing".
We do have a showroom
We have been in business since 1979. That's 37 years !!
It would also need a page or area listing all other services we offer .
We are a full service glass shop. Here are some of the
services and products we offer
Shower Doors- Frameless, Sliding ,Semi Framed, Splash Panels
Shower door repair
Mirrors- clear, colored and antique for - exersize areas, gyms, bathrooms, door mirrors, dressing areas, frames,bars and backsplashes
Glass for table tops and furniture tops
Patterned glass, Painted glass, curved china cabinet glass
Saftey glass- laminated and tempered
Plexiglass
Storm and screens repaired
Fogged insulated glass replaced
Picture frame glass, window glass , plate glass
All types of glass replacement
Fireplace and wood stove glass
Showcase glass
Holes drilled for aquariums
And much more

Target Market(s)

Homeowners / (second area contractors)

Industry/Entity Type

It Company

Font styles to use
Serif

Requirements
Must have
• Photos- more traditional , some modern, brief description under /next to some photos. One page listing other services we provide
• Brief bio of who we are- family business serving Greenwich and surrouding communities since 1978.(will elaborate more when needed)
Nice to have
• Check glass company and shower door websites for ideas
• ms spray panel,
• regalclearview shower doors westport ct.
• Tovrin glass - good wording and copy
Should not have
• We do not do any commercial buildings a residential theme should be used.
• we do not do web sales
• we are not a bargain/ discount business
• do not put call now for a estimate
• pictures of product not people
• No Mailing space area. If mailed I will use a envelope.

```html
<!DOCTYPE html>
<html lang="en">
<head>
<meta charset="utf-8">
<title>Brightpane Co. Inc. – Trifold Brochure</title>
<link href="https://fonts.googleapis.com/css2?family=Oswald:wght@400;500;700&family=Open+Sans:wght@400;600&display=swap" rel="stylesheet">
<style>
  :root{
    --canvas:#d9d9d9;
    --paper-light:#f6f6f6;
    --paper-mid:#e2e2e2;
    --charcoal:#2a2a2a;
    --charcoal-2:#444;
    --accent:#2e9fd8;
    --accent-dark:#1c7fb5;
    --ink:#2b2b2b;
    --ink-soft:#555;
    --white:#ffffff;
    --ember:#6b1510;
    --ember-light:#b2412a;
  }
  *{box-sizing:border-box;margin:0;padding:0}
  html,body{width:1200px;height:1200px;overflow:hidden;background:var(--canvas)}
  body{font-family:"Open Sans",Arial,sans-serif;color:var(--ink)}
  .spread{position:absolute;left:51px;top:178px;width:1098px;height:844px;display:flex;box-shadow:0 12px 30px rgba(0,0,0,.25)}
  .panel{position:relative;width:366px;height:844px;overflow:hidden;background:linear-gradient(160deg,var(--paper-light),var(--paper-mid))}
  .panel + .panel{border-left:1px solid rgba(0,0,0,.08)}
  .panel-art{position:absolute;inset:0;width:366px;height:844px}
  .heading{font-family:"Oswald",Arial,sans-serif;text-transform:uppercase}

  /* services panel */
  .services{position:absolute;left:28px;top:96px;width:316px;font-size:10.5px;line-height:1.45}
  .services-title{font-size:20px;font-weight:500;color:var(--ink);margin-bottom:8px}
  .pricing-pill{display:inline-block;background:var(--accent);color:var(--white);font-family:"Oswald",Arial,sans-serif;font-size:11px;letter-spacing:.5px;padding:3px 14px;border-radius:12px;margin-bottom:12px}
  .service-group{margin-bottom:9px}
  .service-head{font-family:"Oswald",Arial,sans-serif;font-size:12px;font-weight:500;text-transform:uppercase;display:flex;align-items:center;gap:6px}
  .tick{width:11px;height:11px;flex:none}
  .service-items{display:grid;grid-template-columns:1fr 1fr;column-gap:10px;padding-left:22px;list-style:none;color:var(--ink-soft)}
  .service-items li::before{content:"•";color:var(--accent);margin-right:5px}
  .service-single{padding-left:22px;color:var(--ink-soft);list-style:none}
  .service-single li::before{content:"•";color:var(--accent);margin-right:5px}
  .tag-row{display:flex;gap:6px;margin:10px 0 8px}
  .tag{background:var(--accent);color:var(--white);font-family:"Oswald",Arial,sans-serif;font-size:10.5px;padding:2px 9px}
  .services-more{color:var(--ink-soft);font-size:10.5px}

  /* about panel */
  .about{position:absolute;left:40px;top:222px;width:300px;text-align:left}
  .about-name{font-size:17px;font-weight:500;color:var(--ink);margin-bottom:8px}
  .about-label{font-size:20px;font-weight:500;color:var(--accent);margin-bottom:4px}
  .about-copy{font-size:12px;line-height:1.5;color:var(--ink-soft);margin-bottom:18px}
  .contact-phone{display:flex;align-items:center;gap:8px;font-family:"Oswald",Arial,sans-serif;font-size:28px;font-weight:400;color:var(--ink)}
  .contact-address{display:flex;gap:8px;font-size:14px;line-height:1.35;color:var(--ink);margin-top:4px}
  .icon{width:16px;height:16px;flex:none;margin-top:2px}
  .web{position:absolute;left:0;width:100%;text-align:center;font-size:14px;color:var(--white);letter-spacing:.3px}
  .about-web{bottom:46px}

  /* cover panel */
  .brand{position:absolute;right:28px;top:58px;text-align:right;color:var(--white);font-family:"Oswald",Arial,sans-serif;font-weight:500;font-size:34px;line-height:1;letter-spacing:1px;text-transform:uppercase}
  .headline{position:absolute;left:36px;top:540px;width:310px;font-family:"Oswald",Arial,sans-serif;text-transform:uppercase}
  .headline-place{font-size:66px;font-weight:700;color:var(--accent);line-height:1}
  .headline-sub{font-size:32px;font-weight:400;color:var(--ink);line-height:1.1}
  .cover-web{bottom:40px}
</style>
</head>
<body>
<main class="spread">

  <!-- Inside panel: services -->
  <section class="panel panel-services">
    <svg class="panel-art" viewBox="0 0 366 844" aria-hidden="true">
      <defs>
        <linearGradient id="roomTones" x1="0" y1="0" x2="1" y2="1">
          <stop offset="0" stop-color="#f3eee2"/><stop offset=".6" stop-color="#d9c59a"/><stop offset="1" stop-color="#b89a5f"/>
        </linearGradient>
      </defs>
      <path d="M0 0H366V18Q190 28 0 86Z" fill="var(--charcoal)"/>
      <path d="M0 92Q190 32 366 24" fill="none" stroke="var(--accent)" stroke-width="5"/>
      <path d="M0 844V740Q170 790 366 760V844Z" fill="var(--charcoal)"/>
      <path d="M0 732Q170 782 366 752" fill="none" stroke="var(--white)" stroke-width="4"/>
    </svg>
    <svg class="panel-art" viewBox="0 0 366 844">
      <circle cx="72" cy="690" r="98" fill="var(--accent)"/>
      <circle cx="72" cy="690" r="88" fill="url(#roomTones)" role="img" aria-label="Photo of a bright bathroom with glass shower enclosure"/>
    </svg>
    <div class="services">
      <h2 class="services-title heading">Services we offer :</h2>
      <div class="pricing-pill">We are competitive in our pricing</div>

      <div class="service-group">
        <div class="service-head"><svg class="tick" viewBox="0 0 12 12"><path d="M1 6l3 3 7-7" fill="none" stroke="var(--accent)" stroke-width="2"/></svg>Shower doors :</div>
        <ul class="service-items"><li>Frameless</li><li>Splash panels</li><li>Sliding</li><li>Shower door repair</li><li>Semi framed</li></ul>
      </div>
      <div class="service-group">
        <div class="service-head"><svg class="tick" viewBox="0 0 12 12"><path d="M1 6l3 3 7-7" fill="none" stroke="var(--accent)" stroke-width="2"/></svg>Mirrors : clear, colored and antique for :</div>
        <ul class="service-items"><li>Exercise areas</li><li>Dressing areas</li><li>Gyms</li><li>Frames</li><li>Bathrooms</li><li>Bars</li><li>Door mirrors</li><li>Backsplashes</li></ul>
      </div>
      <div class="service-group">
        <div class="service-head"><svg class="tick" viewBox="0 0 12 12"><path d="M1 6l3 3 7-7" fill="none" stroke="var(--accent)" stroke-width="2"/></svg>Glass for table tops and furniture tops :</div>
        <ul class="service-items"><li>Patterned glass</li><li>Curved china cabinet</li><li>Painted glass</li></ul>
      </div>
      <div class="service-group">
        <div class="service-head"><svg class="tick" viewBox="0 0 12 12"><path d="M1 6l3 3 7-7" fill="none" stroke="var(--accent)" stroke-width="2"/></svg>Safety glass - laminated and tempered</div>
        <ul class="service-single"><li>Plexiglass</li><li>Storm and screens repaired</li><li>Fogged insulated glass replaced</li></ul>
      </div>
      <div class="tag-row"><span class="tag">Picture frame glass</span><span class="tag">Window glass</span><span class="tag">Plate glass</span></div>
      <p class="services-more">All types of glass replacement. Fireplace and wood stove glass. Showcase glass. Holes drilled for aquariums. And much more.</p>
    </div>
  </section>

  <!-- Inside panel: about & contact -->
  <section class="panel panel-about">
    <svg class="panel-art" viewBox="0 0 366 844">
      <defs>
        <linearGradient id="showerTones" x1="0" y1="0" x2="1" y2="1">
          <stop offset="0" stop-color="#d8ece9"/><stop offset=".6" stop-color="#9fc9c3"/><stop offset="1" stop-color="#2f3638"/>
        </linearGradient>
      </defs>
      <path d="M0 0H366V40Q170 46 0 120Z" fill="var(--charcoal)" aria-hidden="true"/>
      <path d="M0 126Q170 54 366 46" fill="none" stroke="var(--accent)" stroke-width="5" aria-hidden="true"/>
      <circle cx="252" cy="112" r="80" fill="var(--accent)"/>
      <circle cx="252" cy="112" r="70" fill="url(#showerTones)" role="img" aria-label="Photo of a modern frameless glass shower"/>
      <rect x="40" y="520" width="290" height="142" rx="16" fill="#efe9d8" stroke="var(--accent)" stroke-width="4" role="img" aria-label="Street map showing the shop location in Cos Cob"/>
      <path d="M0 844V736Q180 700 366 724V844Z" fill="var(--accent)" aria-hidden="true"/>
      <path d="M0 728Q180 692 366 716" fill="none" stroke="var(--white)" stroke-width="4" aria-hidden="true"/>
    </svg>
    <div class="about">
      <h2 class="about-name heading">Brightpane Co. Inc.</h2>
      <h3 class="about-label heading">Who we are :</h3>
      <p class="about-copy">Family business serving Greenwich and surrounding communities since 1978.</p>
      <h3 class="about-label heading">Contact us :</h3>
      <p class="contact-phone"><svg class="icon" viewBox="0 0 16 16"><path d="M4 1l3 3-2 2q1 3 5 5l2-2 3 3-2 3Q3 14 1 3Z" fill="var(--accent)"/></svg>203-514-7381</p>
      <p class="contact-address"><svg class="icon" viewBox="0 0 16 16"><path d="M8 1L1 7h2v8h4v-5h2v5h4V7h2Z" fill="var(--accent)"/></svg><span>185 West Harlow Rd.<br>Cos Cob, Ct. 06812</span></p>
    </div>
    <p class="web about-web">www.brightpaneinc.com</p>
  </section>

  <!-- Front cover -->
  <section class="panel panel-cover">
    <svg class="panel-art" viewBox="0 0 366 844">
      <defs>
        <radialGradient id="emberTones" cx=".6" cy=".45" r=".8">
          <stop offset="0" stop-color="var(--ember-light)"/><stop offset=".6" stop-color="var(--ember)"/><stop offset="1" stop-color="#2a0806"/>
        </radialGradient>
        <linearGradient id="bathTones" x1="0" y1="0" x2="1" y2="1">
          <stop offset="0" stop-color="#c9b27a"/><stop offset=".5" stop-color="#eef0e6"/><stop offset="1" stop-color="#8c9b8a"/>
        </linearGradient>
      </defs>
      <path d="M0 0H366V300Q190 340 0 430Z" fill="url(#emberTones)" role="img" aria-label="Warm red abstract light backdrop"/>
      <path d="M0 440Q190 350 366 312" fill="none" stroke="var(--accent)" stroke-width="8" aria-hidden="true"/>
      <path d="M0 456Q190 370 366 334" fill="none" stroke="var(--charcoal)" stroke-width="6" aria-hidden="true"/>
      <circle cx="196" cy="372" r="116" fill="var(--accent)"/>
      <circle cx="196" cy="372" r="104" fill="url(#bathTones)" role="img" aria-label="Photo of a bathroom with soaking tub and glass window"/>
      <path d="M0 844V718Q190 744 366 770V844Z" fill="var(--charcoal)" aria-hidden="true"/>
      <path d="M0 702Q190 728 366 754" fill="none" stroke="var(--white)" stroke-width="5" aria-hidden="true"/>
      <path d="M0 692Q190 718 366 744" fill="none" stroke="var(--charcoal-2)" stroke-width="3" aria-hidden="true"/>
    </svg>
    <p class="brand">Brightpane<br>Co., Inc.</p>
    <h1 class="headline">
      <span class="headline-place">Greenwich</span><br>
      <span class="headline-sub">CT shower doors<br>and bathrooms</span>
    </h1>
    <p class="web cover-web">www.brightpaneinc.com</p>
  </section>

</main>
</body>
</html>
```